Harborline Supply Company Business Card Design

The Business Card will be one side only with Harborline Supplies Company Logo
Card should have:
Name
Title
Office phone Number
Cell Number
email address
Website
Street Address
Our Slogan is Rugged and Reliable
Looking for something that stands out from other business cards

Target Market(s)

Heavy equipment Lease Company

```html
<!DOCTYPE html>
<html lang="en">
<head>
<meta charset="utf-8">
<title>Harborline Supplies Company – Business Card</title>
<link rel="stylesheet" href="https://fonts.googleapis.com/css2?family=Open+Sans:wght@400;600;700&family=Merriweather:wght@400&display=swap">
<style>
  :root{
    --page:#e9e7e4;
    --card-white:#ffffff;
    --brand-red:#d0283c;
    --deep-red:#7c0d16;
    --bright-red:#c8303e;
    --navy:#2a2f7a;
    --ink:#4a4a4a;
    --muted:#777777;
    --rule:#e4a2aa;
  }
  *{box-sizing:border-box;margin:0;padding:0}
  html,body{width:1200px;height:1200px;overflow:hidden;background:var(--page)}
  body{display:flex;flex-direction:column;align-items:center;justify-content:center;gap:60px;font-family:"Open Sans",Arial,sans-serif}
  .card{width:840px;height:480px;position:relative;overflow:hidden;box-shadow:0 8px 24px rgba(0,0,0,.18)}

  /* Front */
  .card-front{background:var(--card-white)}
  .name-marker{position:absolute;left:0;top:52px;width:34px;height:58px;background:var(--navy)}
  .person{position:absolute;left:54px;top:52px}
  .person-name{font-family:"Merriweather",Georgia,serif;font-size:34px;color:var(--brand-red);letter-spacing:1px;line-height:1.1}
  .person-title{font-size:17px;color:var(--muted);margin-top:4px}
  .contact{position:absolute;left:54px;top:150px;font-size:17px;color:var(--ink);list-style:none}
  .contact li{display:flex;align-items:center;gap:10px;margin-bottom:7px}
  .contact svg{width:16px;height:16px;flex:none}
  .contact-web{position:absolute;left:330px;top:222px;font-size:17px;color:var(--ink);list-style:none;border-left:1px solid var(--rule);padding-left:14px}
  .contact-web li{display:flex;align-items:center;gap:10px;margin-bottom:7px}
  .contact-web svg{width:16px;height:16px;flex:none}
  .accent{color:var(--brand-red)}
  .rule-line{position:absolute;left:0;top:318px;width:840px;height:1px;background:var(--rule)}
  .slogan-band{position:absolute;left:0;bottom:0;width:640px;height:150px;background:linear-gradient(90deg,var(--brand-red),#d83a4c);display:flex;align-items:flex-start;padding:26px 0 0 50px}
  .slogan{color:#fff;font-size:20px;font-weight:600;letter-spacing:9px;text-transform:uppercase}
  .brand-main{position:absolute;right:60px;top:160px;display:flex;align-items:center;gap:14px}
  .brand-dot{width:40px;height:40px;border-radius:50%;background:var(--navy)}
  .brand-name{font-size:24px;font-weight:700;color:var(--brand-red);text-transform:uppercase;letter-spacing:.5px;line-height:1.15;width:260px}
  .brand-sub{position:absolute;right:46px;top:380px;display:flex;align-items:center;gap:8px}
  .brand-sub .brand-dot{width:20px;height:20px}
  .brand-sub-name{font-size:13px;font-weight:700;color:var(--brand-red);text-transform:uppercase}

  /* Back */
  .card-back{background:radial-gradient(ellipse at 50% 45%,var(--bright-red) 0%,#a51d2a 55%,var(--deep-red) 100%);display:flex;align-items:center;justify-content:center}
  .back-brand{display:flex;flex-direction:column;align-items:center;gap:10px}
  .back-brand-name{font-size:40px;font-weight:700;color:#fff;text-transform:uppercase;letter-spacing:1px}
  .back-rule{width:520px;height:2px;background:rgba(255,255,255,.85)}
</style>
</head>
<body>

<section class="card card-front" aria-label="Business card front">
  <div class="name-marker"></div>
  <div class="person">
    <h1 class="person-name">JOHN DOE</h1>
    <p class="person-title">Director</p>
  </div>

  <ul class="contact">
    <li>
      <svg viewBox="0 0 16 16"><path d="M8 1a5 5 0 0 0-5 5c0 4 5 9 5 9s5-5 5-9a5 5 0 0 0-5-5zm0 7a2 2 0 1 1 0-4 2 2 0 0 1 0 4z" fill="var(--brand-red)"/></svg>
      Dummy city, Dummy Country Land
    </li>
    <li>
      <svg viewBox="0 0 16 16"><path d="M2 6c0-2 3-3 6-3s6 1 6 3l-2 1-1-2H5L4 7zM4 8h8l1 5H3z" fill="var(--brand-red)"/></svg>
      1-234-567890
    </li>
    <li>
      <svg viewBox="0 0 16 16"><rect x="4" y="1" width="8" height="14" rx="1.5" fill="var(--brand-red)"/><rect x="5.5" y="3" width="5" height="8" fill="#fff"/></svg>
      1-234-567890
    </li>
  </ul>

  <ul class="contact-web">
    <li>
      <svg viewBox="0 0 16 16"><circle cx="8" cy="8" r="6.5" fill="none" stroke="var(--brand-red)" stroke-width="1.6"/><path d="M1.5 8h13M8 1.5c3 3 3 10 0 13M8 1.5c-3 3-3 10 0 13" fill="none" stroke="var(--brand-red)" stroke-width="1.2"/></svg>
      <span>www.<span class="accent">harborlinesupply</span>.com</span>
    </li>
    <li>
      <svg viewBox="0 0 16 16"><rect x="1" y="3" width="14" height="10" rx="1" fill="var(--brand-red)"/><path d="M1.5 3.5 8 9l6.5-5.5" fill="none" stroke="#fff" stroke-width="1.3"/></svg>
      <span>john@<span class="accent">harborlinesupply</span>.com</span>
    </li>
  </ul>

  <div class="rule-line"></div>

  <div class="slogan-band"><p class="slogan">Rugged and Reliable</p></div>

  <div class="brand-main">
    <div class="brand-dot"></div>
    <p class="brand-name">Harborline Supplies Company</p>
  </div>

  <div class="brand-sub">
    <div class="brand-dot"></div>
    <p class="brand-sub-name">Keelwater Pumps</p>
  </div>
</section>

<section class="card card-back" aria-label="Business card back">
  <div class="back-brand">
    <p class="back-brand-name">Harborline Supplies Company</p>
    <div class="back-rule"></div>
  </div>
</section>

</body>
</html>
```